Marlo’s Sandwich Corner Grand Opening Door Flyer

1. Project Title
• “Flyer Design for Sandwich Shop Grand Opening”
• Why it’s effective: Direct and to the point, highlighting the purpose of the design.

2. Project Description
• “We’re looking for a professional designer to create a vibrant and modern flyer for our sandwich shop, Marlo’s Corner. The flyer should emphasize our handcrafted sandwiches, fresh-baked bread, and house-made meats. As a women & family-owned business, we want this aspect prominently displayed. The flyer should also include our logo, a ‘Grand Opening’ and our website: MarlosCorner.com. We want the design to be clean, bold, and visually appealing to attract customers. We also would like a QR code so they can scan to load of the website to order online, but also list it.
• Why it’s effective: Clear goals, modern style preference, and necessary details outlined.

3. Visual Style
• “Modern, bold, and clean design with bright, appetizing colors. Focus on high-quality imagery of sandwiches, sleek fonts, and an inviting layout.”
• Why it’s effective: Communicates the desired aesthetic and tone.

4. Key Details to Include
• Business Name: Marlo’s Sandwich Corner
• Taglines:
“Women & Family Owned”
“Handcrafted Sandwiches Made with Love”
“Fresh Baked Bread”
“House-made Slow Roasted House Specialties”
“Gluten-Friendly”
“Vegan-Friendly”
“7:00am Fresh Daily Grounded Coffee and Breakfast”

• Call-to-Action: “Order Online at MarlosCorner.com”
• Placeholder for the logo.
• Size: 4.25 x 11 (Door Hanger)
• File Format: High-resolution PDF, JPEG, or PNG.
• Print-Ready: Include bleed margins and ensure print clarity.

6. Tone
• Friendly and professional. Highlighting that your business is women-owned adds a unique and personal touch vs deli meat shops. We are a gourmet sandwich shop, with fresh baked bread, house-made meats, with gluten and vegan options. Each sandwich is made with love.

Target Market(s)

Coffee drinkers for morning crowd and sandwiches for lunch

Industry/Entity Type

Sandwich Shop

Colors
EB3D1F
EC4F4E
F09395
F8D3D4
FCEDEE

Requirements
Must have
• See Description
Nice to have
• Use website to get a feel for color theme
Should not have
• NA

```html
<!DOCTYPE html>
<html lang="en">
<head>
<meta charset="utf-8">
<title>Marlo’s Sandwich Corner – Grand Opening Door Hanger</title>
<link rel="stylesheet" href="https://fonts.googleapis.com/css2?family=Montserrat:wght@400;500;600;700;800&display=swap">
<style>
  :root {
    --backdrop: #666666;
    --orange: #eb4d22;
    --charcoal: #222222;
    --charcoal-soft: #2b2b2b;
    --white: #ffffff;
    --blush: #f8d3d4;
    --ink: #1a1a1a;
    --line: rgba(255,255,255,0.18);
  }
  * { margin: 0; padding: 0; box-sizing: border-box; }
  html, body {
    width: 900px; height: 1200px; overflow: hidden;
    background: var(--backdrop);
    font-family: "Montserrat", Arial, sans-serif;
  }
  .canvas { position: relative; width: 900px; height: 1200px; }
  .hanger {
    position: absolute; left: 238px; top: 53px;
    width: 412px; height: 1064px;
    background: var(--white); overflow: hidden;
  }
  .hanger > * { position: absolute; }

  .brand {
    left: 0; width: 100%; top: 38px; text-align: center;
    color: var(--orange); font-weight: 800; font-size: 34px; line-height: 1.05;
  }
  .brand small { display: block; font-size: 15px; letter-spacing: 1.5px; text-transform: uppercase; }

  .door-slot { left: 0; top: 120px; width: 310px; height: 140px; }

  .lower-panel { left: 0; top: 382px; width: 100%; height: 605px; background: var(--charcoal); }
  .stripes { top: 400px; width: 22px; height: 70px;
    background: repeating-linear-gradient(to bottom, var(--orange) 0 6px, transparent 6px 14px); }
  .stripes--left { left: 0; }
  .stripes--right { right: 0; }

  .headline {
    left: 0; width: 100%; top: 226px; text-align: center;
    color: var(--orange); font-weight: 700; font-size: 68px; letter-spacing: 2px; line-height: 1;
    padding-left: 4px;
  }
  .frame { left: 22px; top: 282px; width: 365px; height: 280px; background: var(--orange); }
  .frame-label {
    left: 0; width: 100%; top: 288px; text-align: center;
    color: var(--white); font-size: 19px; font-weight: 400;
  }
  .storefront-photo {
    left: 34px; top: 317px; width: 340px; height: 265px;
    border: 2px solid var(--white);
    background: linear-gradient(to bottom, #e9e9e9 0%, #d6d6d6 22%, #1f1f1f 30%, #2a2a2a 45%, #9aa3a6 60%, #6f7679 100%);
  }

  .hours-hooks { left: 270px; top: 580px; width: 120px; height: 32px; }
  .hours-box {
    left: 267px; top: 604px; width: 120px; height: 117px;
    border: 3px solid var(--orange);
    color: var(--white); text-align: center; line-height: 1.1; padding-top: 10px;
  }
  .hours-box .time { font-weight: 700; font-size: 16px; }
  .hours-box .lead { font-size: 14px; }
  .hours-box .tiny { font-size: 10px; }
  .hours-box .big { font-size: 19px; }
  .hours-box .and { font-size: 11px; }

  .owned { left: 20px; top: 620px; color: var(--white); }
  .owned .women { color: var(--orange); font-weight: 700; font-size: 48px; line-height: 1; letter-spacing: 1px; }
  .owned .family { font-size: 21px; font-weight: 500; margin-top: 5px; padding-left: 9px; }

  .ribbon {
    left: 0; top: 709px; width: 251px; height: 27px;
    background: var(--blush); color: var(--ink);
    font-size: 11px; font-weight: 500; line-height: 27px; padding-left: 13px;
    letter-spacing: -0.2px; white-space: nowrap;
    clip-path: polygon(0 0, 100% 0, 96% 100%, 0 100%);
  }

  .features { left: 0; top: 745px; width: 412px; height: 240px;
    background: radial-gradient(ellipse at 50% 55%, var(--charcoal-soft), var(--charcoal)); }
  .features .divider-v { position: absolute; left: 205px; top: 6px; width: 1px; height: 230px; background: var(--line); }
  .features .divider-h { position: absolute; left: 0; top: 122px; width: 412px; height: 1px; background: var(--line); }
  .feature { position: absolute; width: 206px; text-align: center; color: var(--white); font-size: 12.5px; line-height: 1.2; }
  .feature svg { display: block; margin: 0 auto 10px; }
  .feature--roast { left: 0; top: 18px; }
  .feature--bread { left: 206px; top: 18px; }
  .feature--vegan { left: 0; top: 135px; }
  .feature--gluten { left: 206px; top: 135px; }

  .cta-label {
    left: 0; top: 987px; width: 100%; height: 25px; background: var(--white);
    text-align: center; color: var(--ink); font-size: 18px; font-weight: 500; line-height: 25px;
  }
  .cta-url {
    left: 0; top: 1012px; width: 100%; height: 52px; background: var(--orange);
    text-align: center; color: var(--white); font-size: 30px; font-weight: 700; line-height: 48px;
  }
</style>
</head>
<body>
<main class="canvas">
  <article class="hanger">
    <div class="brand">Marlo’s<small>Sandwich Corner</small></div>

    <svg class="door-slot" viewBox="0 0 310 140" aria-hidden="true">
      <rect x="0" y="22" width="252" height="60" fill="#666666"/>
      <circle cx="252" cy="52" r="53" fill="#666666"/>
    </svg>

    <div class="lower-panel"></div>
    <div class="stripes stripes--left"></div>
    <div class="stripes stripes--right"></div>

    <h1 class="headline">GRAND</h1>
    <div class="frame"></div>
    <p class="frame-label">opening</p>
    <div class="storefront-photo" role="img" aria-label="Photo of the shop storefront with its sign and black awning, the owners celebrating out front"></div>

    <svg class="hours-hooks" viewBox="0 0 120 32" aria-hidden="true">
      <line x1="30" y1="0" x2="30" y2="28" stroke="#eb4d22" stroke-width="2"/>
      <line x1="82" y1="0" x2="82" y2="28" stroke="#eb4d22" stroke-width="2"/>
      <circle cx="30" cy="27" r="3.5" fill="#eb4d22"/>
      <circle cx="82" cy="27" r="3.5" fill="#eb4d22"/>
    </svg>
    <div class="hours-box">
      <div class="time">7:00am</div>
      <div class="lead">Fresh Daily</div>
      <div class="tiny">Grounded</div>
      <div class="big">Coffee</div>
      <div class="and">and</div>
      <div class="lead">Breakfast</div>
    </div>

    <div class="owned">
      <div class="women">WOMEN</div>
      <div class="family">and family owned</div>
    </div>
    <div class="ribbon">Handcrafted Sandwiches Made with Love</div>

    <section class="features">
      <div class="divider-v"></div>
      <div class="divider-h"></div>
      <div class="feature feature--roast">
        <svg width="52" height="44" viewBox="0 0 52 44" aria-hidden="true">
          <path d="M20 2c-3 4 3 6 0 10M26 2c-3 4 3 6 0 10M32 2c-3 4 3 6 0 10" stroke="#eb4d22" stroke-width="2" fill="none"/>
          <path d="M4 28 Q26 10 48 28 Z" fill="#eb4d22"/>
          <rect x="2" y="28" width="48" height="5" rx="2" fill="#eb4d22"/>
          <path d="M6 34 H46 L42 42 H10 Z" fill="#eb4d22"/>
        </svg>
        House-made Slow Roasted<br>House&nbsp; Specialties
      </div>
      <div class="feature feature--bread">
        <svg width="52" height="44" viewBox="0 0 52 44" aria-hidden="true">
          <path d="M14 14 L26 4 L38 14 Z" fill="#eb4d22"/>
          <rect x="4" y="16" width="44" height="4" rx="2" fill="#eb4d22"/>
          <path d="M8 21 H44 V34 Q44 42 36 42 H16 Q8 42 8 34 Z" fill="#eb4d22"/>
          <rect x="1" y="24" width="7" height="4" fill="#eb4d22"/>
          <rect x="44" y="24" width="7" height="4" fill="#eb4d22"/>
        </svg>
        Fresh Baked Breadrafted<br>Sandwiches Made with Love
      </div>
      <div class="feature feature--vegan">
        <svg width="44" height="44" viewBox="0 0 44 44" aria-hidden="true">
          <circle cx="22" cy="22" r="19" stroke="#eb4d22" stroke-width="3" fill="none"/>
          <line x1="22" y1="12" x2="22" y2="34" stroke="#eb4d22" stroke-width="2.5"/>
          <ellipse cx="17" cy="18" rx="3" ry="5" fill="#eb4d22" transform="rotate(-30 17 18)"/>
          <ellipse cx="27" cy="18" rx="3" ry="5" fill="#eb4d22" transform="rotate(30 27 18)"/>
          <ellipse cx="17" cy="26" rx="3" ry="5" fill="#eb4d22" transform="rotate(-30 17 26)"/>
          <ellipse cx="27" cy="26" rx="3" ry="5" fill="#eb4d22" transform="rotate(30 27 26)"/>
          <line x1="9" y1="35" x2="35" y2="9" stroke="#eb4d22" stroke-width="3"/>
        </svg>
        Vegan-Friendly
      </div>
      <div class="feature feature--gluten">
        <svg width="44" height="44" viewBox="0 0 44 44" aria-hidden="true">
          <path d="M20 40 C4 34 4 16 18 6 C24 18 26 30 20 40 Z" fill="#eb4d22"/>
          <path d="M24 38 C26 26 30 16 40 10 C44 24 36 36 24 38 Z" fill="#eb4d22"/>
        </svg>
        Gluten-Friendly
      </div>
    </section>

    <p class="cta-label">Order Online at</p>
    <p class="cta-url">MarlosCorner.com</p>
  </article>
</main>
</body>
</html>
```